Harrowgate Construction And Masonry Ltd

Black background

Logo - attached

Services (bullet points)
New Builds
Extensions
Refurbishments
Alterations
Brickwork Specialists

Contact details - 01632 960418 or 0791 5530274

Email address - contact@harrowgateconstructionandmasonry.co.uk

Website - www.harrowgateconstructionandmasonry.co.uk

Facebook logo

```html
<!DOCTYPE html>
<html lang="en">
<head>
<meta charset="utf-8">
<title>Harrowgate Construction And Masonry Ltd – Flyer</title>
<link href="https://fonts.googleapis.com/css2?family=Barlow+Semi+Condensed:wght@700;800&family=Montserrat:wght@400;500;600;700&display=swap" rel="stylesheet">
<style>
  :root{
    --stage:#8a8a8a;
    --ink:#0d1719;
    --green:#1fdc78;
    --white:#ffffff;
    --social:#3b52a8;
  }
  *{box-sizing:border-box;margin:0;padding:0}
  html,body{width:1200px;height:900px;overflow:hidden;background:var(--stage);font-family:"Montserrat",sans-serif}
  .flyer{
    position:absolute;left:30px;top:49px;width:1008px;height:710px;
    background:var(--ink);transform:scale(1.131);transform-origin:0 0;overflow:hidden;
  }
  .brand{position:absolute;left:36px;top:38px;width:220px;text-align:center;color:var(--white)}
  .brand-mark{width:52px;height:52px;background:var(--green);margin:0 auto 20px}
  .brand-name{font-weight:600;font-size:29px;letter-spacing:1.5px;line-height:1}
  .brand-sub{font-weight:500;font-size:8.4px;color:var(--green);letter-spacing:.3px;margin-top:5px}
  .headline-band{position:absolute;left:0;top:208px;width:420px;height:190px}
  .headline{position:absolute;left:38px;top:222px;color:var(--ink);font-family:"Barlow Semi Condensed",sans-serif;font-weight:800;font-size:48px;line-height:56px;letter-spacing:.2px}
  .hero{position:absolute;left:248px;top:36px;width:726px;height:408px}
  .services-title{position:absolute;left:38px;top:414px;color:var(--white);font-family:"Barlow Semi Condensed",sans-serif;font-weight:800;font-size:30px;letter-spacing:.3px}
  .services{position:absolute;left:38px;top:455px;display:flex;gap:15px;list-style:none}
  .service{width:175px;text-align:center;color:var(--white)}
  .service svg{display:block}
  .service-label{height:62px;display:flex;align-items:center;justify-content:center;font-weight:400;font-size:21px;line-height:28px;letter-spacing:.4px}
  .contact-bar{
    position:absolute;left:0;top:658px;width:1008px;height:47px;background:var(--green);
    display:flex;align-items:center;justify-content:center;gap:14px;color:var(--ink);
    font-weight:700;font-size:11.6px;letter-spacing:-.2px;
  }
  .contact-item{display:flex;align-items:center;gap:4px;white-space:nowrap}
  .contact-icon{width:19px;height:19px;flex:none}
  .social-dot{width:21px;height:21px;border-radius:50%;background:var(--social);flex:none}
</style>
</head>
<body>
<main class="flyer">
  <svg class="headline-band" viewBox="0 0 420 190" aria-hidden="true">
    <polygon points="0,0 318,0 398,190 0,190" fill="var(--green)"/>
  </svg>

  <div class="brand">
    <div class="brand-mark"></div>
    <div class="brand-name">HARROWGATE</div>
    <div class="brand-sub">CONSTRUCTION AND MASONRY LTD</div>
  </div>

  <h1 class="headline">BUILDING &amp;<br>BRICKWORK<br>SPECIALIST’S</h1>

  <svg class="hero" viewBox="0 0 726 408" role="img" aria-label="Photo of a bright open-plan kitchen extension with skylights, exposed brick chimney, garden glazing and large white island">
    <defs>
      <linearGradient id="heroFill" x1="0" y1="0" x2=".35" y2="1">
        <stop offset="0" stop-color="#eef0ef"/>
        <stop offset=".22" stop-color="#d9dbd8"/>
        <stop offset=".42" stop-color="#8f9a7c"/>
        <stop offset=".58" stop-color="#9a7a5c"/>
        <stop offset=".72" stop-color="#d8d8d4"/>
        <stop offset=".86" stop-color="#6a4630"/>
        <stop offset="1" stop-color="#3b2a22"/>
      </linearGradient>
    </defs>
    <polygon points="1,1 655,1 725,36 725,407 161,407" fill="none" stroke="var(--green)" stroke-width="1.5"/>
    <polygon points="12,7 652,7 719,40 719,401 165,401" fill="url(#heroFill)"/>
  </svg>

  <h2 class="services-title">OUR SERVICES</h2>

  <ul class="services">
    <li class="service">
      <svg width="175" height="135" viewBox="0 0 175 135" role="img" aria-label="Photo of a new build timber roof frame under scaffolding">
        <defs><linearGradient id="gNew" x1="0" y1="0" x2="0" y2="1"><stop offset="0" stop-color="#9fc0dc"/><stop offset=".45" stop-color="#d8c39a"/><stop offset="1" stop-color="#6e5a40"/></linearGradient></defs>
        <polygon points="1,1 160,1 174,14 174,134 1,134" fill="none" stroke="var(--green)" stroke-width="1.5"/>
        <polygon points="5,5 157,5 170,17 170,130 5,130" fill="url(#gNew)"/>
      </svg>
      <div class="service-label">New Builds</div>
    </li>
    <li class="service">
      <svg width="175" height="135" viewBox="0 0 175 135" role="img" aria-label="Photo of a house extension under construction">
        <defs><linearGradient id="gExt" x1="0" y1="0" x2="0" y2="1"><stop offset="0" stop-color="#c9c9c6"/><stop offset=".45" stop-color="#a8654e"/><stop offset="1" stop-color="#b79a70"/></linearGradient></defs>
        <polygon points="1,1 160,1 174,14 174,134 1,134" fill="none" stroke="var(--green)" stroke-width="1.5"/>
        <polygon points="5,5 157,5 170,17 170,130 5,130" fill="url(#gExt)"/>
      </svg>
      <div class="service-label">Extensions</div>
    </li>
    <li class="service">
      <svg width="175" height="135" viewBox="0 0 175 135" role="img" aria-label="Photo of a refurbished grey kitchen with bar stools">
        <defs><linearGradient id="gRef" x1="0" y1="0" x2="0" y2="1"><stop offset="0" stop-color="#d4d4d2"/><stop offset=".5" stop-color="#585a5c"/><stop offset="1" stop-color="#8a5a38"/></linearGradient></defs>
        <polygon points="1,1 160,1 174,14 174,134 1,134" fill="none" stroke="var(--green)" stroke-width="1.5"/>
        <polygon points="5,5 157,5 170,17 170,130 5,130" fill="url(#gRef)"/>
      </svg>
      <div class="service-label">Refurbishments</div>
    </li>
    <li class="service">
      <svg width="175" height="135" viewBox="0 0 175 135" role="img" aria-label="Photo of new timber roof rafters on an existing house">
        <defs><linearGradient id="gAlt" x1="0" y1="0" x2="1" y2="1"><stop offset="0" stop-color="#7e9ec4"/><stop offset=".4" stop-color="#c99a58"/><stop offset="1" stop-color="#8a6a42"/></linearGradient></defs>
        <polygon points="1,1 160,1 174,14 174,134 1,134" fill="none" stroke="var(--green)" stroke-width="1.5"/>
        <polygon points="5,5 157,5 170,17 170,130 5,130" fill="url(#gAlt)"/>
      </svg>
      <div class="service-label">Alterations</div>
    </li>
    <li class="service">
      <svg width="175" height="135" viewBox="0 0 175 135" role="img" aria-label="Photo of red brick pillars built in a garden">
        <defs><linearGradient id="gBrick" x1="0" y1="0" x2="0" y2="1"><stop offset="0" stop-color="#7d9a5a"/><stop offset=".35" stop-color="#b0553e"/><stop offset=".75" stop-color="#9a8470"/><stop offset="1" stop-color="#c2b49a"/></linearGradient></defs>
        <polygon points="1,1 160,1 174,14 174,134 1,134" fill="none" stroke="var(--green)" stroke-width="1.5"/>
        <polygon points="5,5 157,5 170,17 170,130 5,130" fill="url(#gBrick)"/>
      </svg>
      <div class="service-label">Brickwork<br>Specialists</div>
    </li>
  </ul>

  <footer class="contact-bar">
    <span class="contact-item">
      <svg class="contact-icon" viewBox="0 0 20 20" aria-hidden="true"><circle cx="10" cy="10" r="10" fill="var(--ink)"/><path d="M7 5.5l1.6 0 .8 2.6-1.1 .9a7 7 0 0 0 2.7 2.7l.9-1.1 2.6 .8v1.6c0 .6-.5 1-1.1 1A8 8 0 0 1 6 6.6c0-.6.4-1.1 1-1.1z" fill="var(--green)"/></svg>
      01632 960418 or 0791 5530274
    </span>
    <span class="contact-item">
      <svg class="contact-icon" viewBox="0 0 20 20" aria-hidden="true"><circle cx="10" cy="10" r="10" fill="var(--ink)"/><rect x="5" y="6.5" width="10" height="7" rx="1" fill="var(--green)"/><path d="M5.3 7l4.7 3.6L14.7 7" fill="none" stroke="var(--ink)" stroke-width="1"/></svg>
      contact@harrowgateconstructionandmasonry.co.uk
    </span>
    <span class="contact-item">
      <svg class="contact-icon" viewBox="0 0 20 20" aria-hidden="true"><circle cx="10" cy="10" r="10" fill="var(--ink)"/><g fill="none" stroke="var(--green)" stroke-width="1"><circle cx="10" cy="10" r="5.5"/><ellipse cx="10" cy="10" rx="2.4" ry="5.5"/><path d="M4.5 10h11M5.3 7.3h9.4M5.3 12.7h9.4"/></g></svg>
      www.harrowgateconstructionandmasonry.co.uk
    </span>
    <span class="social-dot" role="img" aria-label="Social media page"></span>
  </footer>
</main>
</body>
</html>
```